winelabels - new design - redesign the existing winelabels

we want to redesign our winelabels, but we want to keep the basic idea of the labels. we want to have a connection to the new label (see sample). Only the basic information should be on the main label, all other informations should be on the side, like in the new label.
restrictions - not wider than 12 cm, the high is fexibel.
we have about 12 different pictures we use for our labels. They have two different highst (see samples). we have two different types of bottles. If you need more information, please give response.
May have a look to our homepage and our shop under www.falkenried-obermaier.de

Reason: there are a lot of very good ideas, but we are still looking for the "perfect" idea

Font styles to use
Other font styles liked:
• for the name "falkenried-obermaier" use the font simelar to the design " Riesling or Muscaris" everthing else is open

Requirements
Must have
• a connection between old an new design

```html
<!DOCTYPE html>
<html lang="de">
<head>
<meta charset="utf-8">
<title>falkenried-obermaier – Etiketten</title>
<link href="https://fonts.googleapis.com/css2?family=Cinzel:wght@400;500&family=Cormorant+Garamond:ital,wght@0,400;0,500&family=Open+Sans:wght@400&display=swap" rel="stylesheet">
<style>
  :root{
    --bg-top:#a9a9a9;
    --bg-bottom:#cfcfcf;
    --black-label:#141414;
    --black-label-edge:#0a0a0a;
    --red-label:#5e0a0c;
    --red-label-edge:#3e0506;
    --gold:#c9a44a;
    --gold-light:#e2c577;
    --text-light:#e9e4dc;
    --portrait-a:#7d8aa3;
    --portrait-b:#c2b4a1;
    --flowers-a:#c9302a;
    --flowers-b:#9fb39a;
  }
  *{box-sizing:border-box;margin:0;padding:0}
  html,body{width:801px;height:1200px;overflow:hidden}
  body{
    background:linear-gradient(180deg,var(--bg-top),var(--bg-bottom));
    font-family:"Cormorant Garamond",Georgia,serif;
    position:relative;
  }
  .label-row{
    position:absolute;left:84px;top:606px;
    display:flex;gap:16px;
  }
  .label{
    width:148px;height:190px;position:relative;overflow:hidden;
    color:var(--text-light);
    box-shadow:0 2px 6px rgba(0,0,0,.25);
  }
  .label--black{background:linear-gradient(90deg,var(--black-label-edge),var(--black-label) 40%,var(--black-label-edge))}
  .label--red{background:linear-gradient(90deg,var(--red-label-edge),var(--red-label) 45%,var(--red-label-edge))}

  .artwork{position:absolute;left:0;top:0;bottom:0;width:53px}
  .artwork--portrait{background:linear-gradient(160deg,var(--portrait-b),var(--portrait-a) 55%,var(--portrait-b))}
  .artwork--flowers{background:linear-gradient(170deg,var(--flowers-b),var(--flowers-a) 45%,#e3ddd6)}
  .gold-rule{position:absolute;left:55px;top:0;bottom:0;width:2px;background:var(--gold)}

  .main-info{
    position:absolute;top:0;bottom:0;
    display:flex;flex-direction:column;align-items:center;text-align:center;
  }
  .label--front .main-info{left:57px;right:0}
  .label--side .main-info{left:0;width:90px}

  .brand-mark{
    margin-top:14px;width:20px;height:20px;border-radius:50%;
    border:1.5px solid var(--gold);
  }
  .brand-name{
    margin-top:9px;font-size:9px;font-weight:500;color:var(--gold-light);
    letter-spacing:.1px;white-space:nowrap;
  }
  .wine-name{
    margin-top:30px;font-family:"Cinzel",serif;font-size:13px;letter-spacing:.6px;
    color:var(--text-light);white-space:nowrap;
  }
  .vintage{margin-top:7px;font-size:8px;color:var(--text-light);font-variant-numeric:lining-nums}
  .style{
    position:absolute;bottom:8px;font-family:"Cinzel",serif;font-size:7px;letter-spacing:.4px;
    color:var(--text-light);
  }

  .side-text{
    position:absolute;right:4px;top:14px;bottom:14px;width:50px;
    display:flex;flex-direction:row-reverse;justify-content:space-between;
    color:var(--text-light);
  }
  .side-col{
    writing-mode:vertical-rl;transform:rotate(180deg);
    font-family:"Open Sans",sans-serif;font-size:4.2px;line-height:1.35;
    display:flex;justify-content:space-between;
  }
  .side-col--facts{font-size:5.5px}
  .side-col--facts .side-name{font-family:"Cinzel",serif;font-size:8px}
</style>
</head>
<body>
  <div class="label-row">

    <section class="label label--black label--front">
      <div class="artwork artwork--portrait" role="img" aria-label="Gemälde: Bildnis eines Jungen in blauer Jacke"></div>
      <div class="gold-rule"></div>
      <div class="main-info">
        <div class="brand-mark"></div>
        <div class="brand-name">falkenried-obermaier</div>
        <div class="wine-name">VELANTIS</div>
        <div class="vintage">2015</div>
        <div class="style">TROCKEN</div>
      </div>
    </section>

    <section class="label label--black label--side">
      <div class="main-info">
        <div class="brand-mark"></div>
        <div class="brand-name">falkenried-obermaier</div>
        <div class="wine-name">VELANTIS</div>
        <div class="vintage">2015</div>
        <div class="style">TROCKEN</div>
      </div>
      <div class="side-text">
        <div class="side-col side-col--facts"><span>13,5% Alc/Vol</span><span class="side-name">VELANTIS</span><span>0,75l</span></div>
        <div class="side-col"><span>2015 · Qualitätswein · im Holzfass gereift<br>Robuste Rebsorte aus eigener Lage, kräftig und samtig<br>Dunkle Beeren, feine Würze, weiches Tannin, 12,5 g/l<br>Prämiert von der Kammer</span></div>
      </div>
    </section>

    <section class="label label--red label--front">
      <div class="artwork artwork--flowers" role="img" aria-label="Gemälde: rote Blumen in einer Glasvase"></div>
      <div class="gold-rule"></div>
      <div class="main-info">
        <div class="brand-mark"></div>
        <div class="brand-name">falkenried-obermaier</div>
        <div class="wine-name">MORELIN</div>
        <div class="vintage">2015</div>
        <div class="style">TROCKEN</div>
      </div>
    </section>

    <section class="label label--red label--side">
      <div class="main-info">
        <div class="brand-mark"></div>
        <div class="brand-name">falkenried-obermaier</div>
        <div class="wine-name">MORELIN</div>
        <div class="vintage">2015</div>
        <div class="style">TROCKEN</div>
      </div>
      <div class="side-text">
        <div class="side-col side-col--facts"><span>13,5% Alc/Vol</span><span class="side-name">MORELIN</span><span>0,75l</span></div>
        <div class="side-col"><span>2015 · Qualitätswein · im Holzfass gereift<br>Robuste Rebsorte aus eigener Lage, kräftig und samtig<br>Dunkle Beeren, feine Würze, weiches Tannin, 12,5 g/l<br>Prämiert von der Kammer</span></div>
      </div>
    </section>

  </div>
</body>
</html>
```